www.kmtjobfinders.com RE-DESIGN with WordPress

We need to update our current site to WordPress and will also need to add several pages. We will not be very picky on the style and elements as long as the colors and logos are the same-- AL INFO ON SITE WILL STAY THE SAME...CURRENT SITE IS VERY OUTDATED.

The project will consist of using the current site as template (all pics, text etc) and then transferring all the info into a more up to date version. We will also need to add the following functions:

1.) Job Listings page of the current openings our recruitment agency is working on (Must be easily edited and changed) and will allow candidate to submit their resumes via a simple email link)

2.) Featured candidate page that highlights one of our current candidates (profile, pic, editable filed so we may paste bio (must be easily edited via word press.

3.) Bio Page of our current Recruiters (4 bios) - Editable so we can make changes

4.) ALL FINAL FILES MUST BE MIGRATED AND UPLOADED VIA THE DESIGNER SO WE CAN MAKE THE SITE.
Updates

Please make the "homepage" a scrolling page that include all the drop down menu categories using the same info on current site. We can edit or scale back the text if needed. Would, like to see new stock photos and photos must scale to fit all the way across screen and also be mobile and tablet friendly.

Target Market(s)

professional

Coding

Coded - Design and coding required

Font styles to use
Sans Serif

Colors
0355a3
ec1f27
000000
1b1b1b

Requirements
Must have
• All the current info on existing site www.kmtjobfinders.com
• Would like to have design with scolling home page such as:
• Did you get earlier message about the design I eliminated? I was hoping for site more like this?
• https://www.talverhire.com/
• https://www.quorvamedia.com.au/lp/seo-analysis/
Nice to have
• Sleek masculine modern feel
Should not have
• No cursive

```html
<!DOCTYPE html>
<html lang="en">
<head>
<meta charset="utf-8">
<title>Kinmont Search Group – Executive Recruitment</title>
<link rel="stylesheet" href="https://fonts.googleapis.com/css2?family=Montserrat:wght@300;400;500;600;700&family=Open+Sans:wght@400;600&display=swap">
<style>
:root{
  --red:#c8101a;
  --red-bright:#ec1f27;
  --ink:#1b1b1b;
  --black:#000000;
  --grey-text:#555555;
  --light:#f2f2f2;
  --line:#d9d9d9;
  --white:#ffffff;
  --footer:#1d1d1f;
}
*{box-sizing:border-box;margin:0;padding:0}
html,body{width:1200px;height:4369px;overflow:hidden}
body{position:relative;background:var(--white);font-family:'Open Sans',Arial,sans-serif;color:var(--ink)}
.abs{position:absolute}
h1,h2,h3,.nav,.btn{font-family:'Montserrat',Arial,sans-serif}

/* header */
.topbar{left:0;top:0;width:1200px;height:96px;background:var(--white)}
.brand{left:130px;top:26px;display:flex;align-items:center;gap:12px}
.brand-dot{width:40px;height:40px;border-radius:50%;background:var(--red)}
.brand-name{font-family:'Montserrat',Arial,sans-serif;font-weight:600;font-size:26px;color:var(--ink)}
.contact-item{top:26px;display:flex;align-items:center;gap:14px;font-family:'Montserrat',Arial,sans-serif}
.contact-icon{width:40px;height:40px;background:var(--red);border-radius:4px;display:flex;align-items:center;justify-content:center}
.contact-item small{display:block;color:var(--red);font-size:14px;font-weight:600}
.contact-item span{display:block;font-size:15px;color:var(--ink)}
.social-round{top:28px;width:38px;height:38px;border-radius:50%;background:var(--red);display:flex;align-items:center;justify-content:center}
.navbar{left:0;top:96px;width:1200px;height:55px;background:var(--red)}
.nav{position:absolute;top:0;left:162px;display:flex;height:55px;align-items:center;gap:36px;color:var(--white);font-size:15px;font-weight:500}
.resume-tab{left:926px;top:96px;width:150px;height:55px;background:#2a2a2a;color:var(--white);display:flex;align-items:center;justify-content:center;gap:8px;font-family:'Montserrat',Arial,sans-serif;font-size:15px;font-weight:600}

/* hero */
.hero{left:0;top:151px;width:1200px;height:740px;background:linear-gradient(180deg,#6b7a8c 0%,#55606e 45%,#2f3640 100%)}
.hero-title{left:0;top:360px;width:1200px;text-align:center;color:var(--white);font-size:47px;line-height:74px;font-weight:300;letter-spacing:1px}
.hero-title b{font-weight:600}

/* about */
.about-photo{left:590px;top:770px;width:610px;height:570px;background:linear-gradient(135deg,#d9d9d9,#a9aeb4)}
.section-title{font-size:39px;font-weight:400;color:var(--ink)}
.section-title b{color:var(--red);font-weight:700}
.about-title{left:90px;top:870px}
.about-text{left:90px;top:930px;width:470px;font-size:12.5px;line-height:26px;color:var(--grey-text)}
.about-text p{margin-bottom:18px}

/* expertise */
.expertise{left:0;top:1340px;width:1200px;height:713px;background:linear-gradient(180deg,#e4e4e4,#cfcfcf)}
.expertise-title{left:0;top:1470px;width:1200px;text-align:center;font-size:46px}
.card{top:1582px;width:325px;height:326px;background:var(--white);text-align:center;padding:38px 26px 0}
.card h3{font-size:22px;font-weight:500;color:var(--red);margin:30px 0 16px}
.card p{font-size:13.5px;line-height:25px;color:var(--grey-text);height:74px;overflow:hidden}
.card .more{display:block;margin-top:22px;font-family:'Montserrat',Arial,sans-serif;font-weight:700;font-size:13px;color:var(--red)}
.slider-btn{top:1720px;width:44px;height:44px;border-radius:50%;border:2px solid #777;background:rgba(255,255,255,.7);display:flex;align-items:center;justify-content:center}

/* guarantee */
.guarantee-photo{left:100px;top:2150px;width:425px;height:425px;border-radius:50%;background:linear-gradient(135deg,#6b7b6a,#3e4d57);border:10px solid var(--white);box-shadow:0 0 0 4px var(--red)}
.guarantee-head{left:580px;top:2155px;font-size:32px;font-weight:600;color:var(--red);letter-spacing:1px}
.guarantee-sub{left:580px;top:2207px;font-size:24px;font-weight:600;color:#333;letter-spacing:1px}
.guarantee-lead{left:580px;top:2254px;font-family:'Montserrat',Arial,sans-serif;font-size:17px;font-weight:500;color:#333}
.guarantee-text{left:580px;top:2292px;width:510px;font-size:14px;line-height:33px;color:var(--grey-text);text-align:justify}
.btn-outline{left:580px;top:2530px;width:198px;height:54px;border:3px solid var(--red);border-radius:28px;display:flex;align-items:center;justify-content:center;gap:10px;color:var(--red);font-size:17px;font-weight:600}

/* testimonials */
.testimonials{left:0;top:2686px;width:1200px;height:634px;background:linear-gradient(135deg,#3a3a3a,#1f1f1f 55%,#3b3d40)}
.testi-title{left:0;top:2890px;width:1200px;text-align:center;color:var(--white);font-size:34px;font-weight:500}
.testi-quote{left:150px;top:2995px;width:900px;text-align:center;color:var(--white);font-size:20px;line-height:36px}
.testi-author{left:0;top:3112px;width:1200px;text-align:center;color:var(--white);font-family:'Montserrat',Arial,sans-serif;font-weight:700;font-size:18px}

/* form */
.form-title{left:0;top:3400px;width:1200px;text-align:center;font-size:38px}
.field{height:46px;border:1px solid var(--line);font-size:12px;color:#444;padding:14px 16px;display:flex;align-items:flex-start;gap:8px}
.field.message{height:201px}
.btn-solid{top:3694px;height:40px;background:var(--red);color:var(--white);display:flex;align-items:center;justify-content:center;gap:10px;font-size:15px;font-weight:600}

/* footer */
.footer-text{top:4145px;width:330px;text-align:center;color:var(--white);font-size:16px;line-height:30px}
.footer-icon{top:4052px;width:82px;height:82px;border-radius:50%;background:#5a5a5c;display:flex;align-items:center;justify-content:center}
.copyright{left:0;top:4266px;width:1200px;text-align:center;color:#cfcfcf;font-size:15px}
.foot-social{top:4304px;width:32px;height:32px;border-radius:50%;border:2px solid #cfcfcf}
</style>
</head>
<body>

<!-- header -->
<header class="abs topbar">
  <div class="abs brand"><div class="brand-dot"></div><div class="brand-name">Kinmont Search Group</div></div>
  <div class="abs contact-item" style="left:508px">
    <div class="contact-icon"><svg width="20" height="20" viewBox="0 0 24 24"><path fill="#fff" d="M6.6 10.8a15 15 0 0 0 6.6 6.6l2.2-2.2c.3-.3.7-.4 1-.2 1.1.4 2.3.6 3.6.6.6 0 1 .4 1 1V20c0 .6-.4 1-1 1A17 17 0 0 1 3 4c0-.6.4-1 1-1h3.5c.6 0 1 .4 1 1 0 1.3.2 2.5.6 3.6.1.3 0 .7-.2 1z"/></svg></div>
    <div><small>Call us anytime</small><span>555-204-7731</span></div>
  </div>
  <div class="abs contact-item" style="left:710px">
    <div class="contact-icon"><svg width="22" height="18" viewBox="0 0 24 18"><rect x="1" y="1" width="22" height="16" fill="none" stroke="#fff" stroke-width="2"/><path d="M1 2l11 8 11-8" fill="none" stroke="#fff" stroke-width="2"/></svg></div>
    <div><small>Send us a mail</small><span>info@kmtjobfinders.com</span></div>
  </div>
  <div class="abs social-round" style="left:968px"></div>
  <div class="abs social-round" style="left:1016px"></div>
  <div class="abs social-round" style="left:1064px"><svg width="16" height="16" viewBox="0 0 16 16"><circle cx="6.5" cy="6.5" r="4.5" fill="none" stroke="#fff" stroke-width="2"/><path d="M10 10l4.5 4.5" stroke="#fff" stroke-width="2"/></svg></div>
</header>
<nav class="abs navbar">
  <div class="nav"><span>Home</span><span>About Us</span><span>Areas Of Expertise</span><span>Guarantee</span><span>Testimonials</span><span>Contact Us</span></div>
</nav>
<div class="abs resume-tab"><svg width="14" height="14" viewBox="0 0 14 14"><circle cx="7" cy="4" r="3" fill="#fff"/><path d="M1 14c0-4 3-6 6-6s6 2 6 6z" fill="#fff"/></svg>Submit Resume</div>

<!-- hero -->
<section class="abs hero" role="img" aria-label="City skyline with downtown office towers at dusk"></section>
<h1 class="abs hero-title">SENIOR LEVEL <b>EXECUTIVE RECRUITMENT</b><br><b>CONSULTANTS</b></h1>
<svg class="abs" style="left:0;top:700px" width="1200" height="240" viewBox="0 0 1200 240">
  <path d="M0 95 C300 40 560 80 820 70 C1000 60 1120 20 1200 0 L1200 240 L0 240Z" fill="var(--red)"/>
  <path d="M0 110 C300 60 560 100 820 92 C1000 86 1120 50 1200 30 L1200 240 L0 240Z" fill="var(--white)"/>
  <path d="M900 240 C1000 160 1100 110 1200 100 L1200 130 C1110 140 1020 180 960 240Z" fill="var(--red)"/>
</svg>

<!-- about -->
<div class="abs about-photo" role="img" aria-label="Smiling recruiter in a white shirt seated with a tablet"></div>
<h2 class="abs section-title about-title">ABOUT <b>US</b></h2>
<div class="abs about-text">
  <p>Kinmont Search Group is dedicated to, and focused on, helping you secure the most talented people in the market. We assess, recruit, develop and engage the best and brightest people for our corporate clients. Our goal is to improve performance at every level within our client companies so that the whole becomes greater than the sum of each individual's expertise.</p>
  <p>Our recruiters have over 75 years of combined recruiting expertise in a wide variety of industries ranging from Sales and Marketing to Clinical Research. This collective industry experience has, over the years, produced invaluable contacts with industry decision makers across all the business arenas we serve.</p>
  <p>Because of this experience and knowledge, our recruiters are current with the trends and trendsetters around the world, thus giving our clients a continuous competitive watermark of a long-term successful agency.</p>
</div>

<!-- expertise -->
<section class="abs expertise" role="img" aria-label="Faded group of business professionals standing in an office"></section>
<h2 class="abs section-title expertise-title">AREAS OF <b>EXPERTISE</b></h2>
<div class="abs card" style="left:90px">
  <svg width="52" height="44" viewBox="0 0 52 44"><g fill="var(--red)"><rect x="4" y="24" width="6" height="16"/><rect x="14" y="16" width="6" height="24"/><rect x="24" y="20" width="6" height="20"/><rect x="34" y="8" width="6" height="32"/><rect x="0" y="40" width="48" height="3"/></g></svg>
  <h3>Sales and Marketing</h3>
  <p>Kinmont Search Group has established and continues to grow one of the largest networks of top sales and marketing talent.</p>
  <span class="more">READ MORE</span>
</div>
<div class="abs card" style="left:440px">
  <svg width="46" height="46" viewBox="0 0 46 46"><g fill="none" stroke="var(--red)" stroke-width="6"><path d="M6 6l12 12M40 6L28 18M6 40l12-12M40 40L28 28"/></g><g fill="var(--red)"><path d="M2 2h14L2 16z"/><path d="M44 2H30l14 14z"/><path d="M2 44h14L2 30z"/><path d="M44 44H30l14-14z"/></g></svg>
  <h3>Sales Force Expansion</h3>
  <p>From 10 sales reps to over 100, some of the biggest names in the Pharmaceutical, Medical, Biotech and Diagnostic fields.</p>
  <span class="more">READ MORE</span>
</div>
<div class="abs card" style="left:786px">
  <svg width="52" height="46" viewBox="0 0 52 46"><rect x="2" y="10" width="48" height="34" rx="5" fill="var(--red)"/><rect x="17" y="3" width="18" height="9" rx="2" fill="none" stroke="var(--red)" stroke-width="4"/><path d="M22 18h8v7h7v8h-7v7h-8v-7h-7v-8h7z" fill="#fff"/></svg>
  <h3>Pharmaceutical</h3>
  <p>Your recruitment agency needs to be as fast paced and adaptive as the industry in which it exist.</p>
  <span class="more">READ MORE</span>
</div>
<div class="abs slider-btn" style="left:10px"><svg width="14" height="14" viewBox="0 0 14 14"><path d="M9 2L4 7l5 5" fill="none" stroke="#555" stroke-width="2"/></svg></div>
<div class="abs slider-btn" style="left:1146px"><svg width="14" height="14" viewBox="0 0 14 14"><path d="M5 2l5 5-5 5" fill="none" stroke="#555" stroke-width="2"/></svg></div>

<!-- guarantee -->
<div class="abs guarantee-photo" role="img" aria-label="Smiling executive in glasses and sweater working at a desk"></div>
<svg class="abs" style="left:6px;top:2360px" width="72" height="36" viewBox="0 0 72 36"><path d="M70 18H6M22 3L5 18l17 15" fill="none" stroke="var(--red)" stroke-width="4"/></svg>
<svg class="abs" style="left:1122px;top:2360px" width="72" height="36" viewBox="0 0 72 36"><path d="M2 18h64M50 3l17 15-17 15" fill="none" stroke="var(--red)" stroke-width="4"/></svg>
<h2 class="abs guarantee-head">GUARANTEE</h2>
<div class="abs guarantee-sub" style="font-family:'Montserrat',Arial,sans-serif">FOR EMPLOYERS</div>
<div class="abs guarantee-lead">What to Expect from Your Executive Search Firm</div>
<p class="abs guarantee-text">An executive search involves a complex process that requires a substantial investment of your time and resources. When you hire a retained executive search firm, you're entitled to receive a high level of service. But what is the difference between a professional, reliable service and a lower quality of service? What are your rights and obligations as a client? Above all, how do you know when you have received excellence in client service?</p>
<div class="abs btn btn-outline"><svg width="18" height="18" viewBox="0 0 18 18"><path d="M2 12l9-9 4 4-9 9H2z" fill="none" stroke="var(--red)" stroke-width="2"/></svg>Read More</div>

<!-- testimonials -->
<section class="abs testimonials" role="img" aria-label="Overhead view of business people at a meeting table with laptops and phones"></section>
<h2 class="abs testi-title">TESTIMONIALS</h2>
<svg class="abs" style="left:572px;top:2940px" width="56" height="40" viewBox="0 0 56 40"><g fill="#fff"><path d="M0 40V22C0 10 6 2 18 0l2 5c-7 2-10 7-10 13h10v22z"/><path d="M30 40V22c0-12 6-20 18-22l2 5c-7 2-10 7-10 13h10v22z"/></g></svg>
<svg class="abs" style="left:60px;top:3002px" width="76" height="36" viewBox="0 0 76 36"><path d="M74 18H6M22 3L5 18l17 15" fill="none" stroke="#fff" stroke-width="4"/></svg>
<svg class="abs" style="left:1064px;top:3002px" width="76" height="36" viewBox="0 0 76 36"><path d="M2 18h68M54 3l17 15-17 15" fill="none" stroke="#fff" stroke-width="4"/></svg>
<p class="abs testi-quote">Over 27 successful searches over a three-year timeframe speak for itself. Your efforts and those of the staff at Kinmont Search Group are exemplary and top-notch, some of the best work I have seen in over 20 years as a human resources executive.</p>
<div class="abs testi-author">Vice President HR Pharmaceuticals</div>

<!-- submit resume -->
<h2 class="abs section-title form-title" style="font-family:'Montserrat',Arial,sans-serif">SUBMIT YOUR <b>RESUME</b></h2>
<div class="abs field" style="left:163px;top:3476px;width:428px">&#9679; First Name</div>
<div class="abs field" style="left:609px;top:3476px;width:431px">&#9679; Last Name</div>
<div class="abs field" style="left:163px;top:3531px;width:428px">&#9632; Address</div>
<div class="abs field message" style="left:609px;top:3531px;width:431px">&#9632; Message :</div>
<div class="abs field" style="left:163px;top:3586px;width:428px">&#9993; Email Address</div>
<div class="abs field" style="left:163px;top:3640px;width:428px">&#9742; Phone Number</div>
<div class="abs btn btn-solid" style="left:414px;width:177px">&#8679; Upload Resume</div>
<div class="abs btn btn-solid" style="left:609px;width:178px">&#10148; Submit</div>

<!-- footer -->
<svg class="abs" style="left:0;top:3740px" width="1200" height="629" viewBox="0 0 1200 629">
  <path d="M0 0 C80 150 260 200 520 190 C800 180 1000 150 1200 200 L1200 629 L0 629Z" fill="#d6d6d6"/>
  <path d="M0 30 C90 170 270 215 520 208 C800 200 1000 175 1200 225 L1200 629 L0 629Z" fill="var(--footer)"/>
  <path d="M0 80 C120 200 300 230 540 228 C820 226 1000 210 1200 250 L1200 270 C1000 235 820 250 540 252 C300 255 120 230 0 120Z" fill="#4a4a4c"/>
</svg>
<div class="abs footer-icon" style="left:256px"><svg width="30" height="38" viewBox="0 0 30 38"><path d="M15 36S3 22 3 14a12 12 0 0 1 24 0c0 8-12 22-12 22z" fill="none" stroke="#fff" stroke-width="2"/><circle cx="15" cy="14" r="4" fill="none" stroke="#fff" stroke-width="2"/></svg></div>
<div class="abs footer-icon" style="left:558px"><svg width="34" height="34" viewBox="0 0 24 24"><path fill="none" stroke="#fff" stroke-width="1.4" d="M6.6 10.8a15 15 0 0 0 6.6 6.6l2.2-2.2c.3-.3.7-.4 1-.2 1.1.4 2.3.6 3.6.6.6 0 1 .4 1 1V20c0 .6-.4 1-1 1A17 17 0 0 1 3 4c0-.6.4-1 1-1h3.5c.6 0 1 .4 1 1 0 1.3.2 2.5.6 3.6.1.3 0 .7-.2 1z"/></svg></div>
<div class="abs footer-icon" style="left:862px"><svg width="36" height="28" viewBox="0 0 36 28"><rect x="2" y="2" width="32" height="24" fill="none" stroke="#fff" stroke-width="2"/><path d="M2 3l16 13L34 3" fill="none" stroke="#fff" stroke-width="2"/></svg></div>
<div class="abs footer-text" style="left:132px">48 Meridian Way, Suite 310<br>Oakdale, CA 95361</div>
<div class="abs footer-text" style="left:434px">Phone: 555-204-7731<br>Fax: (555) 318 0462</div>
<div class="abs footer-text" style="left:738px">Email: info@kmtjobfinders.com<br>Email: support@kmtjobfinders.com</div>
<div class="abs copyright">© 2018 Company Name. All right reserved</div>
<div class="abs foot-social" style="left:530px"></div>
<div class="abs foot-social" style="left:566px"></div>
<div class="abs foot-social" style="left:602px"></div>
<div class="abs foot-social" style="left:638px"></div>

</body>
</html>
```